Graffiti Artist Business Card Design

I need a card with a Galaxy Background, a spray can in the foreground with a "super Nova ring" around it.

Business Name at top left
All personal details below on left

Have fun :)

Industry/Entity Type

Business

Contact Information for Business Card

Business Name: MURAL TIDEWAY
Name: Darrel Pikeman
Title: Head Graffiti Artist
Mobile: 0471 862 195
Email: brackfen_wu@mailpost-example.net
All types of designs from children's themes to detailed and huge! (Italic)

Requirements
Should not have
• Any logo's on the spray can unless you use Mural Tideway. Thanks

```html
<!DOCTYPE html>
<html lang="en">
<head>
<meta charset="utf-8">
<title>Mural Tideway – Business Card</title>
<link rel="stylesheet" href="https://fonts.googleapis.com/css2?family=Audiowide&display=swap">
<style>
  :root {
    --space-deep: #120e2e;
    --space-indigo: #2a2160;
    --nebula-violet: #6a3a9c;
    --nebula-pink: #b873c9;
    --nebula-glow: #e6c6ef;
    --ink-white: #ffffff;
    --art-light: #f1eef6;
    --art-shadow: #b9b2c8;
  }
  * { margin: 0; padding: 0; box-sizing: border-box; }
  html, body {
    width: 1200px;
    height: 695px;
    overflow: hidden;
    background: var(--space-deep);
  }
  .card {
    position: relative;
    width: 1200px;
    height: 695px;
    overflow: hidden;
    font-family: "Audiowide", sans-serif;
    color: var(--ink-white);
    text-transform: uppercase;
  }
  .galaxy-backdrop {
    position: absolute;
    inset: 0;
    background:
      radial-gradient(ellipse 420px 200px at 560px 330px, var(--nebula-glow) 0%, rgba(230,198,239,0) 70%),
      radial-gradient(ellipse 700px 300px at 500px 340px, var(--nebula-pink) 0%, rgba(184,115,201,0) 75%),
      radial-gradient(ellipse 900px 420px at 600px 360px, var(--nebula-violet) 0%, rgba(106,58,156,0) 80%),
      linear-gradient(180deg, var(--space-indigo) 0%, var(--space-deep) 100%);
  }
  .spray-can-art {
    position: absolute;
    left: 780px;
    top: 0;
    width: 400px;
    height: 580px;
    border-radius: 40px;
    background: radial-gradient(ellipse at 60% 65%, var(--art-light) 0%, var(--art-shadow) 55%, rgba(185,178,200,0.25) 100%);
    opacity: 0.85;
  }
  .business-name {
    position: absolute;
    left: 36px;
    top: 52px;
    font-size: 70px;
    line-height: 1;
    letter-spacing: 0;
    white-space: nowrap;
    transform: scaleY(1.15);
    transform-origin: left top;
  }
  .contact-details {
    position: absolute;
    left: 36px;
    top: 377px;
    list-style: none;
    font-size: 25px;
    line-height: 1;
  }
  .contact-details li { height: 59px; white-space: nowrap; }
  .divider-rule {
    position: absolute;
    left: 0;
    top: 620px;
    width: 1200px;
    height: 9px;
    background: var(--ink-white);
  }
  .tagline-band {
    position: absolute;
    left: 0;
    top: 629px;
    width: 1200px;
    height: 66px;
    background: var(--space-deep);
    display: flex;
    align-items: center;
    justify-content: center;
  }
  .tagline {
    font-size: 25px;
    font-style: italic;
    white-space: nowrap;
    letter-spacing: 0.3px;
  }
</style>
</head>
<body>
  <main class="card">
    <div class="galaxy-backdrop" role="img" aria-label="Purple and pink galaxy nebula photograph with stars"></div>
    <div class="spray-can-art" role="img" aria-label="Illustrated spray paint can with swirls and stars forming a supernova ring"></div>

    <h1 class="business-name">MURAL TIDEWAY</h1>

    <ul class="contact-details">
      <li class="person-name">Darrel Pikeman</li>
      <li class="person-title">Head Graffiti Artist</li>
      <li class="phone">Mobile: 0471 862 195</li>
      <li class="email">Email:brackfen_wu@mailpost-example.net</li>
    </ul>

    <div class="divider-rule"></div>
    <footer class="tagline-band">
      <p class="tagline">All types of designs from children's themes to detailed and huge!</p>
    </footer>
  </main>
</body>
</html>
```